Lucid Haven - Need Stationary Design

We need a stationary pack for our new Care company based in the uk
Are corporate colours are Pink and purple
Please use attached logo
Target Market(s)
The Care Industry
Industry/Entity Type
It Company
Contact Information for Business Card
Moira Blythe
Director

```html
<!DOCTYPE html>
<html lang="en">
<head>
<meta charset="utf-8">
<title>Lucid Haven Stationery</title>
<link rel="stylesheet" href="https://fonts.googleapis.com/css2?family=Open+Sans:wght@400;600&display=swap">
<style>
:root{
  --backdrop:#b5a383;
  --paper:#f5f4f2;
  --purple:#8a5cad;
  --purple-deep:#5b3a86;
  --pink:#e0389a;
  --lilac:#b990d6;
  --ink:#4a4a4a;
  --faint:#f0e2ee;
}
*{margin:0;padding:0;box-sizing:border-box}
html,body{width:1200px;height:516px;overflow:hidden}
body{background:var(--backdrop);position:relative;font-family:"Open Sans",Arial,sans-serif;color:var(--ink)}
.piece{position:absolute;background:var(--paper);overflow:hidden}
.wave{position:absolute;left:0;bottom:0;width:100%}
.brand{font-family:"Open Sans",Arial,sans-serif;font-weight:600;color:var(--purple);display:flex;align-items:center;gap:5px;white-space:nowrap}
.brand .dot{border-radius:50%;background:var(--pink);flex:none}
.faint-mark{position:absolute;border-radius:50%;background:var(--faint)}
.contact{font-size:6px;line-height:8.4px;color:var(--ink)}
.contact .row{display:flex;align-items:center;gap:3px}
.contact .ico{width:5px;height:5px;background:var(--purple);border-radius:1px;flex:none}

/* letterhead */
.letterhead{left:34px;top:22px;width:335px;height:474px}
.letterhead .brand{position:absolute;left:45px;top:62px;font-size:10px}
.letterhead .brand .dot{width:8px;height:8px}
.letterhead .contact{position:absolute;left:234px;top:19px;padding-left:6px;border-left:1px solid #c9c9c9}
.letterhead .faint-mark{left:40px;top:190px;width:230px;height:230px}
.letterhead .web{position:absolute;right:26px;bottom:10px;font-size:6px;letter-spacing:1.5px;color:#fff}

/* business card */
.card{left:482px;top:20px;width:164px;height:94px;background:linear-gradient(90deg,var(--purple-deep),#7a4fa6 55%,#e7e2ea 56%)}
.card .name{position:absolute;left:9px;top:7px;font-size:8px;color:#fff;font-weight:600}
.card .title{position:absolute;left:9px;top:17px;font-size:5px;color:#e8dcf2}
.card .contact{position:absolute;left:9px;top:33px;font-size:4.4px;line-height:6.4px;color:#f2eaf7}
.card .contact .ico{width:4px;height:4px;background:#e8dcf2}
.card .brand{position:absolute;left:94px;top:58px;font-size:7px}
.card .brand .dot{width:6px;height:6px}
.card .swoosh{position:absolute;left:72px;top:0;width:24px;height:94px}

/* envelopes */
.envelope-back{left:389px;top:138px;width:374px;height:170px;background:#fff}
.envelope-back .flap{position:absolute;left:0;top:0;width:100%;height:62px;background:var(--purple);border-radius:0 0 18px 18px}
.envelope-back .flap .dot{position:absolute;left:50%;top:18px;width:24px;height:24px;margin-left:-12px;border-radius:50%;background:#fff}
.envelope-front{left:389px;top:322px;width:374px;height:172px}
.envelope-front .brand{position:absolute;left:17px;top:36px;font-size:8px}
.envelope-front .brand .dot{width:7px;height:7px}
.envelope-front .contact{position:absolute;left:17px;top:50px}
.envelope-front .faint-mark{left:250px;top:20px;width:110px;height:110px}

/* folder */
.folder{left:782px;top:12px;width:384px;height:484px;background:linear-gradient(90deg,#e3e2e0,#f2f1ef 6%,#f2f1ef)}
.folder .faint-mark{left:150px;top:40px;width:260px;height:260px;opacity:.6}
.folder .brand{position:absolute;left:0;right:0;top:270px;justify-content:center;font-size:26px;gap:10px}
.folder .brand .dot{width:20px;height:20px}
</style>
</head>
<body>

<section class="piece letterhead">
  <div class="faint-mark" role="img" aria-label="Faint brand emblem watermark"></div>
  <div class="brand"><span class="dot"></span>Lucid Haven</div>
  <div class="contact">
    <div>2140 Willow Crescent</div>
    <div>Leeds, LS6 2QA</div>
    <div class="row"><span class="ico"></span>614 280 3391</div>
    <div class="row"><span class="ico"></span>752 319 4086</div>
    <div class="row"><span class="ico"></span>390 527 6813</div>
    <div class="row"><span class="ico"></span>hello@lucidhaven.com</div>
  </div>
  <svg class="wave" viewBox="0 0 335 40" height="40" preserveAspectRatio="none">
    <path d="M0 16 C90 2 180 6 335 10 L335 40 L0 40Z" fill="var(--lilac)"/>
    <path d="M0 24 C100 8 200 26 335 14 L335 40 L0 40Z" fill="var(--purple)"/>
    <path d="M0 22 C100 6 200 24 335 12" fill="none" stroke="var(--pink)" stroke-width="2.5"/>
    <path d="M0 19 C100 4 200 20 335 9" fill="none" stroke="#fff" stroke-width="1"/>
  </svg>
  <div class="web">www.lucidhaven.com</div>
</section>

<section class="piece card">
  <svg class="swoosh" viewBox="0 0 24 94" preserveAspectRatio="none">
    <path d="M6 0 C22 30 2 60 16 94" fill="none" stroke="var(--pink)" stroke-width="5"/>
    <path d="M12 0 C26 30 8 60 22 94" fill="none" stroke="#fff" stroke-width="1"/>
  </svg>
  <div class="name">Moira Blythe</div>
  <div class="title">Director</div>
  <div class="contact">
    <div>2140 Willow Crescent</div>
    <div>Leeds, LS6 2QA</div>
    <div class="row"><span class="ico"></span>614 280 3391</div>
    <div class="row"><span class="ico"></span>752 319 4086</div>
    <div class="row"><span class="ico"></span>390 527 6813</div>
    <div class="row"><span class="ico"></span>hello@lucidhaven.com</div>
    <div class="row"><span class="ico"></span>www.lucidhaven.com</div>
  </div>
  <div class="brand"><span class="dot"></span>Lucid Haven</div>
</section>

<section class="piece envelope-back">
  <div class="flap"><span class="dot"></span></div>
</section>

<section class="piece envelope-front">
  <div class="faint-mark" role="img" aria-label="Faint brand emblem watermark"></div>
  <div class="brand"><span class="dot"></span>Lucid Haven</div>
  <div class="contact">
    <div>2140 Willow Crescent</div>
    <div>Leeds, LS6 2QA</div>
  </div>
  <svg class="wave" viewBox="0 0 374 34" height="34" preserveAspectRatio="none">
    <path d="M0 12 C100 0 220 6 374 8 L374 34 L0 34Z" fill="var(--lilac)"/>
    <path d="M0 20 C110 6 230 22 374 12 L374 34 L0 34Z" fill="var(--purple)"/>
    <path d="M0 18 C110 4 230 20 374 10" fill="none" stroke="var(--pink)" stroke-width="2.5"/>
    <path d="M0 15 C110 2 230 16 374 7" fill="none" stroke="#fff" stroke-width="1"/>
  </svg>
</section>

<section class="piece folder">
  <div class="faint-mark" role="img" aria-label="Faint brand emblem watermark"></div>
  <div class="brand"><span class="dot"></span>Lucid Haven</div>
  <svg class="wave" viewBox="0 0 384 64" height="64" preserveAspectRatio="none">
    <path d="M0 10 C120 0 260 14 384 20 L384 64 L0 64Z" fill="var(--lilac)"/>
    <path d="M0 26 C120 10 250 38 384 26 L384 64 L0 64Z" fill="var(--purple)"/>
    <path d="M0 24 C120 8 250 36 384 24" fill="none" stroke="var(--pink)" stroke-width="4"/>
    <path d="M0 19 C120 4 250 30 384 19" fill="none" stroke="#fff" stroke-width="1.5"/>
  </svg>
</section>

</body>
</html>
```